Meadowbrook Foundation Brochure

We are looking for a new brochure design for our foundation. The foundation is a nonprofit organization that provides assistance to special needs families in Indiana. We do this by providing ipads, communication software, gas cards, and financial assistance to families for their special needs child.

Target Market(s)

Families

Industry/Entity Type

Foundation

Colors
0355a3
3176b5
34a6d7
9bcb3b

Requirements
Must have
• Clear concise information

```html
<!DOCTYPE html>
<html lang="en">
<head>
<meta charset="utf-8">
<title>Meadowbrook Foundation Brochure</title>
<link href="https://fonts.googleapis.com/css2?family=Open+Sans:wght@400;600;700;800&display=swap" rel="stylesheet">
<style>
:root{
  --navy:#0355a3;
  --blue:#3176b5;
  --sky:#34a6d7;
  --green:#9bcb3b;
  --green-dark:#6fa52a;
  --ink:#3a4654;
  --paper:#ffffff;
  --backdrop:#e9ecef;
}
*{box-sizing:border-box;margin:0;padding:0}
html,body{width:727px;height:1200px;overflow:hidden;background:var(--backdrop);font-family:"Open Sans",Arial,sans-serif}
.spread{position:absolute;left:20px;width:687px;height:530px;display:flex;box-shadow:0 4px 14px rgba(0,0,0,.18);background:var(--paper)}
.spread--outside{top:30px}
.spread--inside{top:620px}
.panel{position:relative;width:229px;height:530px;overflow:hidden;background:var(--paper)}
.panel + .panel{border-left:1px solid rgba(0,0,0,.06)}
.photo{position:absolute;left:0;right:0}
.wave{position:absolute;left:0;bottom:0;width:229px;height:70px;display:block}
.web{position:absolute;bottom:12px;left:0;right:0;text-align:center;color:#fff;font-size:11px;font-weight:700;letter-spacing:.5px}
.brand{display:flex;align-items:center;gap:7px;justify-content:center}
.brand__dot{width:20px;height:20px;border-radius:50%;flex:none}
.brand__name{font-size:13px;font-weight:700;line-height:1.1}
.body-copy{font-size:7.6px;line-height:1.5}

/* outside: story */
.story{background:var(--navy)}
.story__title{position:absolute;top:18px;left:18px;color:var(--green);font-size:22px;font-weight:700}
.story__text{position:absolute;top:56px;left:18px;right:18px;color:#fff}
.story__photo{top:250px;height:150px;background:linear-gradient(160deg,#7fb24a,#3c7a3a 60%,#2f5f8a)}
.story__sign{position:absolute;top:412px;right:18px;text-align:right;color:#fff;font-size:9px;line-height:1.4}
.story__sign strong{display:block;color:var(--green);font-size:12px}

/* outside: back */
.back{background:linear-gradient(180deg,var(--green) 0%,#7fb83a 100%)}
.back__brand{position:absolute;top:32px;left:0;right:0;flex-direction:column}
.back__brand .brand__dot{width:46px;height:46px;background:#fff}
.back__brand .brand__name{color:#fff;font-size:14px;text-align:center}
.back__address{position:absolute;top:128px;left:0;right:0;text-align:center;color:#fff;font-size:9px;line-height:1.5}
.back__photo{top:190px;height:240px;background:linear-gradient(170deg,#c9d9e8,#8aa6c0 55%,#3e5f86)}

/* outside: cover */
.cover__brand{position:absolute;top:26px;left:0;right:0}
.cover__brand .brand__dot{background:var(--sky)}
.cover__brand .brand__name{color:var(--navy)}
.cover__photo{top:70px;height:290px;background:linear-gradient(165deg,#d8c7b3,#9c8a77 50%,#4b5d6e)}
.cover__band{position:absolute;top:372px;left:0;right:0;height:88px;background:var(--navy);padding:14px 16px;color:#fff}
.cover__band p{font-size:15px;font-weight:800;line-height:1.2;text-transform:uppercase}
.cover__band p:first-child{color:var(--green)}

/* inside */
.head{position:absolute;top:0;left:0;right:0;height:46px;padding:12px 16px;color:#fff;font-size:18px;font-weight:700}
.head--green{background:var(--green)}
.head--blue{background:var(--navy)}
.what__text{position:absolute;top:60px;left:16px;right:16px;color:var(--ink)}
.what__call{position:absolute;top:174px;left:16px;right:10px;color:var(--green-dark);font-size:15px;font-weight:700;white-space:nowrap}
.what__photo{top:212px;height:230px;background:linear-gradient(160deg,#9bb7cf,#5b7a99 55%,#2f4a66)}

.diff__title{position:absolute;top:12px;left:14px;color:var(--navy);font-size:18px;font-weight:700}
.diff__text{position:absolute;top:44px;left:14px;right:14px;color:var(--ink)}
.diff__list{position:absolute;top:78px;left:24px;right:14px;color:var(--ink);font-size:7.8px;line-height:1.6}
.diff__circles{position:absolute;top:150px;left:0;right:0;height:260px}
.circle{position:absolute;border-radius:50%;border:3px solid var(--sky)}
.circle--a{left:20px;top:0;width:86px;height:86px;background:linear-gradient(150deg,#c9b9a5,#7d6e5f)}
.circle--b{left:118px;top:16px;width:92px;height:92px;background:linear-gradient(150deg,#a9c58a,#55803a)}
.circle--c{left:14px;top:100px;width:92px;height:92px;background:linear-gradient(150deg,#b8c8d8,#56708c)}
.circle--d{left:120px;top:120px;width:84px;height:84px;background:linear-gradient(150deg,#d6c2a8,#8a7058)}
.diff__foot{position:absolute;left:0;right:0;bottom:0;height:100px;background:var(--navy)}
.diff__brand{position:absolute;bottom:26px;left:0;right:0}
.diff__brand .brand__dot{background:var(--green)}
.diff__brand .brand__name{color:#fff}

.help__text{position:absolute;top:58px;left:16px;right:16px;color:var(--ink)}
.help__ask{position:absolute;top:124px;left:16px;right:16px;color:var(--navy);font-size:9.5px;font-weight:700;line-height:1.4}
.help__ask span{color:var(--green-dark)}
.steps{position:absolute;top:168px;left:16px;right:16px;list-style:none}
.steps li{display:flex;gap:8px;align-items:flex-start;margin-bottom:10px;color:var(--ink);font-size:7.8px;line-height:1.45}
.steps b{flex:none;width:16px;height:16px;background:var(--sky);color:#fff;font-size:9px;display:flex;align-items:center;justify-content:center}
.help__photo{top:290px;height:170px;background:linear-gradient(160deg,#cfa8a0,#9a6f6a 50%,#3d5f86)}
</style>
</head>
<body>

<section class="spread spread--outside">
  <article class="panel story">
    <h2 class="story__title">The story</h2>
    <p class="story__text body-copy">Meadowbrook Foundation began when one family saw how hard it was to find help for a child with special needs. Today we stand beside families across Indiana, offering tools, support and hope. Every device, card and grant we give helps a child learn, speak and grow, and helps parents feel they are not alone on the road ahead.</p>
    <div class="photo story__photo" role="img" aria-label="Photo of families and children gathered on a lawn"></div>
    <p class="story__sign"><strong>Dana Whitfield</strong>Founder</p>
  </article>

  <article class="panel back">
    <div class="brand back__brand">
      <span class="brand__dot"></span>
      <span class="brand__name">Meadowbrook<br>Foundation</span>
    </div>
    <p class="back__address">1840 Orchard Lane<br>Fairview, IN 46000<br>555-214-0187</p>
    <div class="photo back__photo" role="img" aria-label="Photo of a parent smiling with two children"></div>
    <svg class="wave" viewBox="0 0 229 70" preserveAspectRatio="none" aria-hidden="true">
      <path d="M0 18 Q115 -6 229 22 V70 H0Z" fill="var(--green)"/>
      <path d="M0 28 Q115 6 229 32 V70 H0Z" fill="var(--navy)"/>
    </svg>
    <p class="web">meadowbrookfdn.org</p>
  </article>

  <article class="panel cover">
    <div class="brand cover__brand">
      <span class="brand__dot"></span>
      <span class="brand__name">Meadowbrook Foundation</span>
    </div>
    <div class="photo cover__photo" role="img" aria-label="Photo of a mother holding her young daughter outdoors"></div>
    <svg class="wave" style="top:350px;height:26px" viewBox="0 0 229 26" preserveAspectRatio="none" aria-hidden="true">
      <path d="M0 12 Q115 30 229 4 V26 H0Z" fill="var(--green)"/>
      <path d="M0 20 Q115 34 229 14 V26 H0Z" fill="var(--sky)"/>
    </svg>
    <div class="cover__band">
      <p>Providing hope</p>
      <p>for special needs families</p>
    </div>
    <svg class="wave" viewBox="0 0 229 70" preserveAspectRatio="none" aria-hidden="true">
      <path d="M0 20 Q115 50 229 14 V70 H0Z" fill="var(--sky)"/>
      <path d="M0 36 Q115 62 229 30 V70 H0Z" fill="var(--green)"/>
    </svg>
  </article>
</section>

<section class="spread spread--inside">
  <article class="panel what">
    <h2 class="head head--green">What we do</h2>
    <p class="what__text body-copy">Meadowbrook Foundation is a nonprofit that assists special needs families in Indiana. We provide tablets, communication software, gas cards and financial help so each child can reach their full potential. Our team works closely with parents to find the support that fits.</p>
    <p class="what__call">Call Us at 555 214 0187</p>
    <div class="photo what__photo" role="img" aria-label="Photo of a father with his son"></div>
    <svg class="wave" viewBox="0 0 229 70" preserveAspectRatio="none" aria-hidden="true">
      <path d="M0 18 Q115 -6 229 22 V70 H0Z" fill="var(--green)"/>
      <path d="M0 28 Q115 6 229 32 V70 H0Z" fill="var(--navy)"/>
    </svg>
    <p class="web">meadowbrookfdn.org</p>
  </article>

  <article class="panel diff">
    <h2 class="diff__title">Making A Difference</h2>
    <p class="diff__text body-copy">Below are a few of the children we have assisted through the foundation. We assist families by:</p>
    <ul class="diff__list">
      <li>Purchasing tablets</li>
      <li>Purchasing language software</li>
      <li>Providing gas cards</li>
      <li>Providing a bike for therapy</li>
    </ul>
    <div class="diff__circles">
      <div class="circle circle--a" role="img" aria-label="Photo of a child the foundation has helped"></div>
      <div class="circle circle--b" role="img" aria-label="Photo of a child playing outdoors"></div>
      <div class="circle circle--c" role="img" aria-label="Photo of a child using a tablet"></div>
      <div class="circle circle--d" role="img" aria-label="Photo of a child with a parent"></div>
    </div>
    <div class="diff__foot"></div>
    <svg class="wave" style="bottom:88px;height:26px" viewBox="0 0 229 26" preserveAspectRatio="none" aria-hidden="true">
      <path d="M0 14 Q115 -4 229 10 V26 H0Z" fill="var(--green)"/>
      <path d="M0 20 Q115 4 229 18 V26 H0Z" fill="var(--navy)"/>
    </svg>
    <div class="brand diff__brand">
      <span class="brand__dot"></span>
      <span class="brand__name">Meadowbrook Foundation</span>
    </div>
  </article>

  <article class="panel help">
    <h2 class="head head--blue">How can you help?</h2>
    <p class="help__text body-copy">Consider making a donation to the Meadowbrook Foundation. All donations go directly to families in need. You can give online or by mail, and every gift is tax deductible.</p>
    <p class="help__ask">Do you have a special needs child?<br><span>You may qualify for a grant. To find out:</span></p>
    <ol class="steps">
      <li><b>1</b>Visit meadowbrookfdn.org and complete a grant inquiry form.</li>
      <li><b>2</b>Complete the entire grant application.</li>
      <li><b>3</b>Your application will be reviewed by the foundation and you will be contacted with more information.</li>
    </ol>
    <div class="photo help__photo" role="img" aria-label="Photo of a mother and son playing with a red ball"></div>
    <svg class="wave" viewBox="0 0 229 70" preserveAspectRatio="none" aria-hidden="true">
      <path d="M0 18 Q115 -6 229 22 V70 H0Z" fill="var(--green)"/>
      <path d="M0 28 Q115 6 229 32 V70 H0Z" fill="var(--navy)"/>
    </svg>
  </article>
</section>

</body>
</html>
```